Brisk Comet- Energy shot - ....Amazing Energy for Amazing people

To design a creative /unique logo and picture for Brisk Comet Energy/ energy shot product similar to Zippo Day energy shot...Berry flavor

I want the design to cover the entire bottle. in addition to Logo (Brisk Comet Energy )

So Brisk Comet Energy will be a competitor of Zippo Day energy and I want a creative,fantastic, attractive design to catch customers eyes, the product will be in similar size 2oz bottle (see attached image). This template is based on a common 2oz bottle size that measures exactly 114mm circumference x 83mm-85mm height (including cap ).
Please include At the top cap a Logo for: Brisk Comet...

Target Market(s)

Young, busy professionals, athletics

Industry/Entity Type

Product

Logo Text

Quorva Energy...Amazing Energy &Taste !

Requirements
Must have
• Creative exciting design...Quorva Energy...Fan
Nice to have
• Be a genius....Be creative...Be Amazing !

```html
<!DOCTYPE html>
<html lang="en">
<head>
<meta charset="utf-8">
<title>Quorva Energy Shots – 2 oz bottle label</title>
<link rel="stylesheet" href="https://fonts.googleapis.com/css2?family=Open+Sans:wght@700;800&family=Crimson+Text:wght@600&display=swap">
<style>
  :root {
    --page: #ffffff;
    --label-light: #f1f6fa;
    --label-mid: #cfe3f1;
    --label-blue: #8cc6ea;
    --label-deep: #5fb1e4;
    --brand-red: #e8392f;
    --perforation: #4b4f8a;
  }
  * { margin: 0; padding: 0; box-sizing: border-box; }
  html, body {
    width: 1200px;
    height: 1000px;
    overflow: hidden;
    background: var(--page);
  }
  .canvas {
    position: relative;
    width: 1200px;
    height: 1000px;
    background: var(--page);
  }
  .bottle-label {
    position: absolute;
    left: 330px;
    top: 70px;
    width: 540px;
    height: 860px;
    overflow: hidden;
    border-radius: 6px;
  }
  .label-pattern {
    position: absolute;
    inset: 0;
    background:
      linear-gradient(118deg, transparent 0 38%, rgba(95,177,228,0.55) 38% 52%, transparent 52%),
      linear-gradient(62deg, transparent 0 55%, rgba(140,198,234,0.45) 55% 70%, transparent 70%),
      linear-gradient(160deg, var(--label-light) 0%, var(--label-mid) 45%, var(--label-blue) 75%, var(--label-light) 100%);
  }
  .cap-perforation {
    position: absolute;
    left: 0;
    top: 150px;
    width: 100%;
    height: 4px;
  }
  .badge {
    position: absolute;
    left: 50%;
    top: 290px;
    transform: translateX(-50%);
    display: flex;
    align-items: center;
    gap: 12px;
    font-family: "Crimson Text", Georgia, serif;
    font-weight: 600;
    font-size: 22px;
    line-height: 1.35;
    color: var(--brand-red);
    text-align: center;
    white-space: nowrap;
  }
  .badge-dot {
    width: 18px;
    height: 18px;
    border: 2px solid var(--brand-red);
    border-radius: 50%;
    flex: none;
  }
  .brand-name {
    position: absolute;
    left: 0;
    width: 100%;
    top: 470px;
    text-align: center;
    font-family: "Open Sans", Arial, sans-serif;
    font-weight: 800;
    font-size: 104px;
    letter-spacing: 2px;
    line-height: 1;
    color: var(--brand-red);
  }
  .product-line {
    position: absolute;
    left: 0;
    width: 100%;
    top: 600px;
    text-align: center;
    font-family: "Open Sans", Arial, sans-serif;
    font-weight: 700;
    font-size: 52px;
    line-height: 1;
    color: var(--brand-red);
  }
  .volume {
    position: absolute;
    left: 0;
    width: 100%;
    top: 760px;
    text-align: center;
    font-family: "Crimson Text", Georgia, serif;
    font-weight: 600;
    font-size: 26px;
    color: var(--brand-red);
  }
</style>
</head>
<body>
  <main class="canvas">
    <section class="bottle-label">
      <div class="label-pattern" role="img" aria-label="Soft pale blue and white faceted ribbon pattern wrapping the bottle"></div>
      <svg class="cap-perforation" viewBox="0 0 540 4" preserveAspectRatio="none" aria-hidden="true">
        <line x1="0" y1="2" x2="540" y2="2" stroke="var(--perforation)" stroke-width="3" stroke-dasharray="9 9"/>
      </svg>
      <div class="badge">
        <span class="badge-dot"></span>
        <span class="badge-name">Brisk Comet<br>Energy</span>
      </div>
      <h1 class="brand-name">QUORVA</h1>
      <p class="product-line">ENERGY SHOTS</p>
      <p class="volume">2 oz</p>
    </section>
  </main>
</body>
</html>
```